CCTV Website

We are looking for a Wordpress designer to create an e-commerce website for us. We have all the products that will be uploaded to site on csv format, so our main focus is layout, style, home page slider image selections and related site page images selection by the designer.

When project is reaching completion we will provide product files.

Industry/Entity Type

E-Commerce

```html
<!DOCTYPE html>
<html lang="en">
<head>
<meta charset="utf-8">
<title>Kestrel Securities</title>
<link href="https://fonts.googleapis.com/css2?family=Montserrat:wght@400;600;700&family=PT+Sans:wght@400;700&display=swap" rel="stylesheet">
<style>
:root{
  --blue:#1a6fb8;
  --blue-dark:#135a98;
  --orange:#e8582a;
  --ink:#222;
  --muted:#555;
  --grey-bg:#efefef;
  --footer:#262626;
  --white:#fff;
  --line:#ddd;
}
*{box-sizing:border-box;margin:0;padding:0}
html,body{width:1200px;height:3509px;overflow:hidden}
body{font-family:"PT Sans",sans-serif;color:var(--ink);background:var(--white);position:relative}
.heading{font-family:"Montserrat",sans-serif;font-weight:700;text-transform:uppercase}
.btn{position:absolute;background:var(--blue);color:var(--white);font-family:"Montserrat",sans-serif;font-weight:700;font-size:14px;letter-spacing:.5px;text-transform:uppercase;display:flex;align-items:center;justify-content:center}
.section-title{position:absolute;left:0;width:1200px;text-align:center;color:var(--blue);font-family:"Montserrat",sans-serif;font-weight:700;font-size:23px;text-transform:uppercase}
.section-title::after{content:"";display:block;width:66px;height:2px;background:#c9d6e4;margin:14px auto 0}

/* hero */
.hero{position:absolute;left:0;top:0;width:1200px;height:630px;background:linear-gradient(100deg,#9c7b6c 0%,#c45a4a 22%,#d9c8bd 45%,#c9b9ae 70%,#7d6a62 100%)}
.hero-photo{position:absolute;inset:0;background:linear-gradient(180deg,rgba(255,255,255,.12),rgba(0,0,0,.25))}
.brand{position:absolute;color:var(--white);font-family:"Montserrat",sans-serif;font-weight:700;font-size:26px;letter-spacing:.5px;text-transform:uppercase}
.main-nav{position:absolute;top:20px;right:100px;display:flex;gap:8px}
.main-nav span{color:var(--white);font-family:"Montserrat",sans-serif;font-weight:700;font-size:12px;padding:6px 9px;text-transform:uppercase}
.main-nav .active{background:var(--white);color:var(--ink)}
.hero-title{position:absolute;left:0;top:412px;width:1206px;text-align:center;color:var(--white);font-size:33px;line-height:46px;letter-spacing:.5px}
.hero .btn{left:535px;top:537px;width:128px;height:36px;border:2px solid var(--white);font-size:13px}
.slider-arrow{position:absolute;top:305px;width:30px;height:32px;background:#333;display:flex;align-items:center;justify-content:center}

/* why */
.why-kicker{position:absolute;left:0;top:675px;width:1200px;text-align:center;font-family:"Montserrat",sans-serif;font-weight:700;font-size:16px}
.why-title{top:703px}
.why-photo{position:absolute;left:131px;top:786px;width:465px;height:388px;background:linear-gradient(135deg,#bcd2f0 0%,#7fa4de 40%,#3e5f9c 75%,#2a3b5a 100%)}
.why-text{position:absolute;left:667px;top:805px;width:410px;font-size:15px;line-height:24px;color:var(--muted)}
.why-list{position:absolute;left:667px;top:870px;list-style:none}
.why-list li{height:38.4px;font-size:14.5px;color:var(--ink);padding-left:26px;position:relative}
.why-list li::before{content:"";position:absolute;left:4px;top:6px;border-left:6px solid var(--ink);border-top:4px solid transparent;border-bottom:4px solid transparent}
.why .btn{left:671px;top:1117px;width:113px;height:33px;font-size:12px}

/* features */
.features{position:absolute;left:0;top:1242px;width:1200px;height:553px;background:var(--grey-bg)}
.feature{position:absolute;width:240px}
.feature svg{position:absolute;left:0;top:0}
.feature h3{position:absolute;left:58px;top:0;font-family:"Montserrat",sans-serif;font-weight:600;font-size:14.5px;white-space:nowrap}
.feature p{position:absolute;left:58px;top:26px;width:180px;font-size:12px;line-height:16px;color:var(--muted)}
.feature-rule{position:absolute;height:1px;width:230px;background:var(--line)}
.dome-photo{position:absolute;left:375px;top:1370px;width:355px;height:380px;background:linear-gradient(180deg,#e4e4e4 0%,#d2d2d2 45%,#a9a9a9 80%,#e6e6e6 100%)}

/* trust */
.trust{position:absolute;left:0;top:1796px;width:1200px;height:462px;background:linear-gradient(90deg,var(--blue-dark),var(--blue) 50%,#2a7fc6)}
.trust-title{position:absolute;left:0;top:56px;width:1200px;text-align:center;color:var(--white);font-size:23px}
.trust-title::after{content:"";display:block;width:66px;height:2px;background:rgba(255,255,255,.45);margin:14px auto 0}
.trust-item{position:absolute;color:var(--white)}
.trust-item svg{position:absolute;left:0;top:0}
.trust-item h3{position:absolute;left:58px;top:0;font-family:"Montserrat",sans-serif;font-weight:600;font-size:14.5px;white-space:nowrap}
.trust-item p{position:absolute;left:58px;top:26px;width:290px;font-size:12px;line-height:17px;color:rgba(255,255,255,.85)}

/* testimonials */
.testimonials-title{top:2307px}
.quote-card{position:absolute;top:2405px;width:435px;height:254px;border:2px solid #e6e6e6;background:var(--white)}
.quote-mark{position:absolute;font-family:Georgia,serif;font-size:60px;color:#c8c8c8;line-height:1}
.quote-card p{position:absolute;left:63px;top:40px;width:320px;font-size:13px;line-height:20px;color:var(--muted)}
.stars{position:absolute;left:63px;top:156px;color:#d9392b;font-size:13px;letter-spacing:1px}
.avatar{position:absolute;left:56px;top:186px;width:36px;height:36px;border-radius:50%;background:linear-gradient(135deg,#b8876a,#6c4a3a)}
.reviewer{position:absolute;left:104px;top:190px;font-size:11px;line-height:14px;color:var(--muted)}
.side-arrow{position:absolute;top:2510px}

/* cta */
.cta{position:absolute;left:0;top:2732px;width:1200px;height:416px;background:linear-gradient(90deg,#1f3d60 0%,#4a6a86 30%,#7f8e9c 50%,#c9cfd4 62%,#8a6b5a 85%,#6a4c3e 100%)}
.cta-title{position:absolute;left:164px;top:96px;color:var(--white);font-size:36px;line-height:44px}
.cta-text{position:absolute;left:164px;top:198px;width:340px;color:var(--white);font-size:14.5px;line-height:22px}
.cta .btn{left:168px;top:285px;width:140px;height:40px;font-size:13px}

/* footer */
.site-footer{position:absolute;left:0;top:3148px;width:1200px;height:361px;background:var(--footer);color:var(--white)}
.footer-brand{left:136px;top:60px;font-size:26px}
.follow{position:absolute;left:182px;top:121px;font-family:"Montserrat",sans-serif;font-weight:700;font-size:11px;text-transform:uppercase}
.social{position:absolute;top:114px;width:26px;height:26px;border-radius:50%;background:var(--blue)}
.footer-head{position:absolute;top:54px;font-family:"Montserrat",sans-serif;font-weight:700;font-size:12px;text-transform:uppercase}
.contact-row{position:absolute;left:489px;font-size:12px;line-height:17px;color:#ddd}
.contact-row svg{position:absolute;left:0;top:2px}
.contact-row span{position:absolute;left:21px;top:0;white-space:nowrap}
.footer-menu{position:absolute;left:716px;top:88px;list-style:none;font-size:12px;line-height:18.5px;color:#ddd}
.email-field{position:absolute;left:861px;top:96px;width:206px;height:40px;background:var(--white);color:#777;font-size:12px;padding:12px 14px}
.site-footer .btn{left:861px;top:155px;width:75px;height:28px;font-size:11px}
.footer-rule{position:absolute;left:130px;top:265px;width:940px;height:1px;background:#4a4a4a}
.copyright{position:absolute;left:0;top:306px;width:1200px;text-align:center;font-size:11px;color:#ccc}
</style>
</head>
<body>

<header class="hero">
  <div class="hero-photo" role="img" aria-label="Blurred office interior with a white bullet security camera in the upper right"></div>
  <div class="brand" style="left:134px;top:16px">Kestrel Securities</div>
  <nav class="main-nav">
    <span class="active">Home</span><span>About Us</span><span>Services</span><span>CCTV</span><span>Gallery</span><span>Blog</span><span>Contact</span>
  </nav>
  <div class="slider-arrow" style="left:0"><svg width="8" height="10"><path d="M7 0 L0 5 L7 10Z" fill="#fff"/></svg></div>
  <div class="slider-arrow" style="right:0"><svg width="8" height="10"><path d="M1 0 L8 5 L1 10Z" fill="#fff"/></svg></div>
  <h1 class="hero-title heading">Secure your business<br>with CCTV cameras</h1>
  <div class="btn">Read More</div>
</header>

<section class="why">
  <div class="why-kicker">WHY CHOOSE</div>
  <h2 class="section-title why-title">Kestrel Securities</h2>
  <div class="why-photo" role="img" aria-label="Close-up of a security camera lens in blue light"></div>
  <p class="why-text">There are many variations of passages of Lorem Ipsum available, but the majority have suffered alteration.</p>
  <ul class="why-list">
    <li>New systems installed</li>
    <li>Full HD technology</li>
    <li>Consultancy services</li>
    <li>Free no-obligation quotation</li>
    <li>System control over the internet</li>
    <li>Existing systems repaired and maintained</li>
  </ul>
  <div class="btn">Read More</div>
</section>

<section class="features">
  <h2 class="section-title" style="top:52px">Features</h2>

  <div class="feature" style="left:117px;top:171px">
    <svg width="30" height="30" viewBox="0 0 30 30" fill="none" stroke="var(--orange)" stroke-width="3" stroke-linecap="round"><path d="M3 11a17 17 0 0 1 24 0"/><path d="M8 16a10 10 0 0 1 14 0"/><circle cx="15" cy="22" r="2.5" fill="var(--orange)" stroke="none"/></svg>
    <h3>WIFI</h3><p>There are many variations of pas sages of Lorem Ipsum.</p>
  </div>
  <div class="feature-rule" style="left:117px;top:252px"></div>
  <div class="feature" style="left:117px;top:284px">
    <svg width="36" height="36" viewBox="0 0 36 36"><rect x="1" y="1" width="34" height="34" rx="6" fill="var(--orange)"/><text x="18" y="24" text-anchor="middle" font-family="Montserrat,sans-serif" font-weight="700" font-size="14" fill="#fff">HD</text></svg>
    <h3>HD</h3><p>There are many variations of pas sages of Lorem Ipsum.</p>
  </div>
  <div class="feature-rule" style="left:117px;top:364px"></div>
  <div class="feature" style="left:117px;top:396px">
    <svg width="30" height="40" viewBox="0 0 30 40"><rect x="5" y="1" width="20" height="38" rx="3" fill="var(--orange)"/><rect x="8" y="6" width="14" height="25" fill="#fff"/><circle cx="15" cy="35" r="1.8" fill="#fff"/></svg>
    <h3>Support Smartphones</h3><p>There are many variations of pas sages of Lorem Ipsum.</p>
  </div>

  <div class="feature" style="left:842px;top:171px">
    <svg width="36" height="36" viewBox="0 0 36 36" fill="none" stroke="var(--orange)" stroke-width="2.5"><circle cx="18" cy="18" r="7"/><path d="M18 2v5M18 29v5M2 18h5M29 18h5M6 6l4 4M26 26l4 4M6 30l4-4M26 10l4-4"/></svg>
    <h3>Day and Night</h3><p>There are many variations of pas sages of Lorem Ipsum.</p>
  </div>
  <div class="feature-rule" style="left:842px;top:252px"></div>
  <div class="feature" style="left:842px;top:284px">
    <svg width="36" height="36" viewBox="0 0 36 36"><circle cx="18" cy="18" r="17" fill="var(--orange)"/><path d="M18 8 L26 22 H10Z" fill="#fff"/><rect x="16.5" y="22" width="3" height="6" fill="#fff"/></svg>
    <h3>Outdoor Environment</h3><p>There are many variations of pas sages of Lorem Ipsum.</p>
  </div>
  <div class="feature-rule" style="left:842px;top:364px"></div>
  <div class="feature" style="left:842px;top:396px">
    <svg width="40" height="40" viewBox="0 0 40 40"><path d="M24 4a10 10 0 0 1 6 18l-1 6h-10l-1-6a10 10 0 0 1 6-18z" fill="var(--orange)"/><rect x="19" y="30" width="10" height="4" fill="var(--orange)"/><path d="M4 16q4 4 0 8M9 14q5 6 0 12" stroke="var(--orange)" stroke-width="2" fill="none"/></svg>
    <h3>Motion Detection</h3><p>There are many variations of pas sages of Lorem Ipsum.</p>
  </div>
</section>
<div class="dome-photo" role="img" aria-label="White dome security camera with dark lens"></div>

<section class="trust">
  <h2 class="trust-title heading">You can trust us</h2>
  <div class="trust-item" style="left:186px;top:176px">
    <svg width="40" height="40" viewBox="0 0 40 40" fill="none" stroke="#fff" stroke-width="3"><path d="M7 24v-4a13 13 0 0 1 26 0v4"/><rect x="5" y="22" width="7" height="11" rx="2" fill="#fff"/><rect x="28" y="22" width="7" height="11" rx="2" fill="#fff"/></svg>
    <h3>24/7 Communication</h3><p>There are many variations of passages of Lorem Ipsum available, but the majority have suffered alteration.</p>
  </div>
  <div class="trust-item" style="left:665px;top:176px">
    <svg width="40" height="40" viewBox="0 0 40 40"><path d="M12 18v-5a8 8 0 0 1 16 0v5" fill="none" stroke="#fff" stroke-width="3.5"/><rect x="8" y="18" width="24" height="18" rx="2" fill="#fff"/></svg>
    <h3>Your Privacy - Our Responsibility</h3><p>There are many variations of passages of Lorem Ipsum available, but the majority have suffered alteration.</p>
  </div>
  <div class="trust-item" style="left:186px;top:321px">
    <svg width="40" height="40" viewBox="0 0 40 40" fill="none" stroke="#fff" stroke-width="3"><circle cx="20" cy="20" r="15"/><path d="M20 11v10h7"/></svg>
    <h3>Perfection in every second</h3><p>There are many variations of passages of Lorem Ipsum available, but the majority have suffered alteration.</p>
  </div>
  <div class="trust-item" style="left:665px;top:321px">
    <svg width="40" height="44" viewBox="0 0 40 44"><text x="20" y="38" text-anchor="middle" font-family="Montserrat,sans-serif" font-weight="700" font-size="42" fill="#fff">$</text></svg>
    <h3>Very Low Cost</h3><p>There are many variations of passages of Lorem Ipsum available, but the majority have suffered alteration.</p>
  </div>
</section>

<section class="testimonials">
  <h2 class="section-title testimonials-title">Testimonials</h2>
  <svg class="side-arrow" style="left:78px" width="14" height="26"><path d="M12 2 L2 13 L12 24" stroke="#ccc" stroke-width="2" fill="none"/></svg>
  <svg class="side-arrow" style="left:1085px" width="14" height="26"><path d="M2 2 L12 13 L2 24" stroke="#ccc" stroke-width="2" fill="none"/></svg>

  <div class="quote-card" style="left:145px">
    <span class="quote-mark" style="left:26px;top:20px">&ldquo;</span>
    <p>Lorem Ipsum is simply dummy text of the printing and typesetting industry. Lorem Ipsum has been the industry's standard dummy text ever since the 1500s, when an unknown printer took a galley of type and scrambled</p>
    <span class="quote-mark" style="left:130px;top:118px">&rdquo;</span>
    <div class="stars">★★★★★</div>
    <div class="avatar" role="img" aria-label="Reviewer portrait"></div>
    <div class="reviewer">Daniel Marsh<br>England</div>
  </div>
  <div class="quote-card" style="left:613px">
    <span class="quote-mark" style="left:26px;top:20px">&ldquo;</span>
    <p>Lorem Ipsum is simply dummy text of the printing and typesetting industry. Lorem Ipsum has been the industry's standard dummy text ever since the 1500s, when an unknown printer took a galley of type and scrambled</p>
    <span class="quote-mark" style="left:130px;top:118px">&rdquo;</span>
    <div class="stars">★★★★★</div>
    <div class="avatar" role="img" aria-label="Reviewer portrait"></div>
    <div class="reviewer">Daniel Marsh<br>England</div>
  </div>
</section>

<section class="cta" role="img" aria-label="Outdoor security camera mounted on a brick wall, blurred background">
  <h2 class="cta-title heading">CCTV for<br>your safety</h2>
  <p class="cta-text">Lorem Ipsum is simply dummy text of the printing and typesetting industry lorem Ipsum has been the industry's standard</p>
  <div class="btn">Read More</div>
</section>

<footer class="site-footer">
  <div class="brand footer-brand">Kestrel Securities</div>
  <div class="follow">Follow Us</div>
  <span class="social" style="left:272px"></span>
  <span class="social" style="left:306px"></span>
  <span class="social" style="left:340px"></span>

  <div class="footer-head" style="left:489px">Contact Us</div>
  <div class="contact-row" style="top:88px">
    <svg width="10" height="13" viewBox="0 0 10 13"><path d="M5 0a5 5 0 0 1 5 5c0 3-5 8-5 8S0 8 0 5a5 5 0 0 1 5-5z" fill="#fff"/><circle cx="5" cy="5" r="1.8" fill="var(--footer)"/></svg>
    <span>118 Foundry Lane<br>Millbrook, IL 60999</span>
  </div>
  <div class="contact-row" style="top:140px">
    <svg width="11" height="11" viewBox="0 0 11 11"><path d="M2 0l2 3-1 1.5a7 7 0 0 0 3.5 3.5L8 7l3 2-1 2C5 11 0 6 0 1z" fill="#fff"/></svg>
    <span>555.010.2040</span>
  </div>
  <div class="contact-row" style="top:177px">
    <svg width="12" height="9" viewBox="0 0 12 9"><rect width="12" height="9" fill="#fff"/><path d="M0 0l6 5 6-5" stroke="var(--footer)" fill="none"/></svg>
    <span>info@kestrelsecurities.com</span>
  </div>

  <div class="footer-head" style="left:716px">Menu</div>
  <ul class="footer-menu">
    <li>Home</li><li>About Us</li><li>Services</li><li>CCTV</li><li>Gallery</li><li>Blog</li><li>Contact</li>
  </ul>

  <div class="footer-head" style="left:861px">Newsletter</div>
  <div class="email-field">E-mail id</div>
  <div class="btn">Signup</div>

  <div class="footer-rule"></div>
  <div class="copyright">Copyrights @ 2018 All Rights Reserved</div>
</footer>

</body>
</html>
```